Maple Harbour Website

We are starting a marketing company and to do that we need a website! We want a website that will inspire and persuade to bring out the awesomeness in our clients.
What we want to see:
- Inspirational and persuasive imagery that relate to Branding.
- No cliche images eg. business man, suits and hand shakes
- We want to transform and educate our clients.
- We want to show them the path and would like our website to really act as a guide that guides them step by step through our process.
- We want the portray that we are an investment but not have a pretentious way to it. We put our heart into every project and that is how we treat our clients.
-When you submit your design please include what platform you have created for. Preference would be Wordpress or Joobla.

We have included the psd file for the wire frame, logo files, font files, site map and a link to a video we create to give you more information on what we would like to see. http://clipvault-example.com/t/qk82LmPzr

Feel free to make small modification to the logos if you think it will improve it. Your creativity and advice is most welcome.
Updates

One thing we forgot. We would like to have our contact information near the top of the website as well as at the bottom.  Here is out contact info:

Email: info@mapleharbour.ca
Phone: 403-555-0142

Reason: As we are new with the platform and that we want to optimize our results, we decided to extend the deadline by 15 days. Thanks!

Target Market(s)

28-60, Male and Female, Oil field, Local Businesses, Dentists, Chiropractors, Hair salon, Construction/Renovation, Events etc

Industry/Entity Type

Investment

Requirements
Must have
• - 4 Inspirational and persuasive Imagery for the top portion of the website
- Must have a feel as if your not on a website an example of this is linked below.
http://www.pixelforum-sample.com/design/472093/web-design-by-helen-dawes
Nice to have
• - Creative advice from you.
- Creative buttons for Get Free Quote and Subscribe buttons. Something out of the box that draws peoples attention. eg. a 'B' button. Just and example but still something related to branding.
Should not have
• No Cliches

```html
<!DOCTYPE html>
<html lang="en">
<head>
<meta charset="utf-8">
<title>Maple Harbour – Strategy</title>
<link href="https://fonts.googleapis.com/css2?family=Arimo:wght@400;700&display=swap" rel="stylesheet">
<style>
:root{
  --navy:#2e3140;
  --navy-tab:#4a5068;
  --muted-nav:#8a8d98;
  --green:#8cc04a;
  --green-dark:#6e9a2f;
  --text-grey:#8a8a8a;
  --heading:#2e3140;
  --link:#1a7fd6;
  --panel:#f2f2f2;
  --white:#ffffff;
  --footer-copy:#7b7f8e;
}
*{box-sizing:border-box;margin:0;padding:0}
html,body{width:1200px;height:823px;overflow:hidden}
body{font-family:"Arimo",Helvetica,Arial,sans-serif;background:var(--white);position:relative}

.top-bar{position:absolute;left:0;top:0;width:1200px;height:41px;background:var(--navy)}
.logo-card{position:absolute;left:118px;top:0;width:189px;height:76px;background:var(--white);display:flex;align-items:center;padding-left:18px;gap:10px;z-index:3}
.logo-square{width:22px;height:22px;background:var(--green);flex:none}
.logo-name{font-weight:700;font-size:19px;line-height:21px;color:#8e8e8e;letter-spacing:.5px}
.site-nav{position:absolute;left:340px;top:0;display:flex;height:41px}
.site-nav a{display:flex;align-items:center;justify-content:center;height:41px;font-size:17px;font-weight:700;color:var(--muted-nav);text-decoration:none;width:150px}
.site-nav a.current{background:var(--navy-tab);color:var(--white);width:142px}
.social{position:absolute;left:955px;top:9px;display:flex;gap:6px}
.social span{width:24px;height:24px;border-radius:4px;background:#5c6174}

.hero{position:absolute;left:0;top:41px;width:1200px;height:294px}
.hero-image{width:100%;height:100%;background:radial-gradient(ellipse at 50% 45%,#6e6e6e 0%,#4a4a4a 55%,#333 100%)}

.main-nav{position:absolute;left:117px;top:274px;display:flex;height:61px}
.main-nav a{width:160px;height:61px;display:flex;align-items:center;justify-content:center;text-align:center;font-size:21px;font-weight:700;color:var(--white);text-decoration:none;background:rgba(60,60,60,.55);border-right:1px dashed rgba(255,255,255,.25)}
.main-nav a.active{background:var(--white);color:var(--heading);width:159px;border-right:none}
.main-nav a.quote{margin-left:2px;width:158px;background:linear-gradient(#9bcb55,var(--green-dark));font-size:18px;line-height:18px;border-right:none}

.content{position:absolute;left:158px;top:366px;width:570px}
.content h1{font-size:22px;font-weight:700;color:var(--heading);margin-bottom:17px}
.content p{font-size:15px;line-height:22px;color:var(--text-grey);margin-bottom:22px}
.content a{color:var(--link);text-decoration:underline}

.newsletter{position:absolute;left:760px;top:408px;width:285px;height:165px;background:var(--panel);border-radius:6px;padding:26px 0 0 50px}
.newsletter h2{font-size:20px;font-weight:700;color:#333;margin-bottom:4px}
.newsletter p{font-size:15px;color:var(--text-grey);margin-bottom:16px}
.subscribe{display:flex;align-items:center;justify-content:center;width:191px;height:46px;background:linear-gradient(#9bcb55,var(--green-dark));border:1px solid #5d8526;color:var(--white);font-size:20px;font-weight:700}

.footer{position:absolute;left:0;top:727px;width:1200px;height:96px;background:var(--navy)}
.footer-links{position:absolute;left:117px;top:15px;display:flex;gap:13px}
.footer-links a{color:var(--white);font-size:15px;text-decoration:none}
.copyright{position:absolute;right:139px;top:17px;font-size:13px;color:var(--footer-copy)}
</style>
</head>
<body>
<header class="top-bar">
  <nav class="site-nav">
    <a class="current" href="#">Maple Harbour</a>
    <a href="#">Be Found</a>
    <a href="#">Connect</a>
    <a href="#">Get Growing</a>
  </nav>
  <div class="social" aria-label="Social links"><span></span><span></span><span></span><span></span></div>
</header>
<div class="logo-card"><span class="logo-square"></span><span class="logo-name">MAPLE<br>HARBOUR.CA</span></div>

<section class="hero">
  <div class="hero-image" role="img" aria-label="Photograph of the word START painted in white on dark asphalt"></div>
</section>
<nav class="main-nav">
  <a class="active" href="#">Strategy</a>
  <a href="#">Portfolio</a>
  <a href="#">About Us</a>
  <a href="#">Contact Us</a>
  <a href="#">Blog</a>
  <a class="quote" href="#">Get a<br>Free Quote</a>
</nav>

<main class="content">
  <h1>Main Headline</h1>
  <p>Morbi ac commodo nulla. In condimentum orci id nisl volutpat bibendum. Quisque commodo hendrerit lorem quis egestas. Maecenas quis tortor arcu. Vivamus rutrum nunc non neque consectetur quis placerat neque lobortis.</p>
  <p>Nam vestibulum, arcu sodales feugiat consectetur, nisl orci bibendum elit, eu euismod magna sapien ut nibh. Donec <a href="#">sample link</a> tortor dictum gravida. In hac habitasse platea dictumst. Nam pulvinar, odio sed rhoncus suscipit, sem diam ultrices mauris, eu consequat purus metus eu velit. Proin metus odio, aliquam eget molestie nec, gravida ut sapien.</p>
  <p>Phasellus quis est sed turpis sollicitudin venenatis sed eu odio. Praesent eget neque.</p>
</main>

<aside class="newsletter">
  <h2>Get Tips and Tricks!</h2>
  <p>Subscribe to our Newsletter.</p>
  <div class="subscribe">Subscribe</div>
</aside>

<footer class="footer">
  <nav class="footer-links">
    <a href="#">Site Map</a><a href="#">Strategy</a><a href="#">Portfolio</a><a href="#">About Us</a><a href="#">Contact Us</a><a href="#">Blog</a>
  </nav>
  <div class="copyright">©MAPLE HARBOUR INC. 2013</div>
</footer>
</body>
</html>
```